Postcard Design

We are a very small nonprofit raising money from lawyers and law firms to support pro bono civil legal services. This postcard is an announcement of our annual fundraising event. It will be mailed to lawyers, judges, and other legal professionals. I'm looking for a clean, uncluttered, conservative design. I am including an event flyer with the details that need to be incorporated on the postcard. I've also included our logo.

Conservative

```html
<!DOCTYPE html>
<html lang="en">
<head>
<meta charset="utf-8">
<title>Annual Fundraiser Postcard – Back</title>
<link rel="stylesheet" href="https://fonts.googleapis.com/css2?family=Roboto+Condensed:wght@400;500&family=Roboto:ital,wght@1,300&display=swap">
<style>
  :root {
    --page-bg: #d9d9d9;
    --card-border: #0a63ad;
    --card-face: #ffffff;
    --accent-blue: #0a5fae;
    --ink: #111111;
    --ink-muted: #7a7a7a;
    --ink-soft: #8a8a8a;
    --panel-grey: #eeeeee;
    --rule: #dcdcdc;
  }
  * { margin: 0; padding: 0; box-sizing: border-box; }
  html, body {
    width: 1200px; height: 1000px; overflow: hidden;
    background: var(--page-bg);
  }
  .postcard {
    position: absolute; left: 70px; top: 40px;
    width: 1088px; height: 840px;
    background: var(--card-border);
  }
  .postcard-face {
    position: absolute; left: 14px; top: 14px;
    width: 1060px; height: 812px;
    background: var(--card-face);
    border-radius: 14px;
    font-family: "Roboto Condensed", "Arial Narrow", sans-serif;
  }
  .message-side { position: absolute; left: 0; top: 0; width: 530px; height: 812px; }
  .honorees-title {
    position: absolute; left: 22px; top: 12px;
    font-size: 31px; font-weight: 500; color: var(--ink-muted);
    text-decoration: underline; text-underline-offset: 4px;
  }
  .award { position: absolute; left: 22px; }
  .award-lifetime { top: 58px; }
  .award-service { top: 232px; }
  .award-name {
    font-size: 27px; font-weight: 500; color: var(--accent-blue); line-height: 33px;
  }
  .honoree-name { font-size: 27px; font-weight: 500; color: var(--ink); line-height: 34px; }
  .honoree-role { font-size: 26px; color: var(--ink-muted); line-height: 33.5px; }
  .registration {
    position: absolute; left: 0; top: 413px;
    width: 513px; height: 147px;
    background: var(--panel-grey);
    padding: 14px 0 0 10px;
    color: var(--ink); font-size: 28px; line-height: 41px;
  }
  .registration-heading { font-weight: 500; }
  .registration strong { font-weight: 500; }
  .registration a { color: var(--ink); font-weight: 500; text-decoration: underline; }
  .mission {
    position: absolute; left: 16px; top: 582px; width: 496px;
    font-family: "Roboto", Arial, sans-serif; font-style: italic; font-weight: 300;
    font-size: 24.5px; line-height: 33.5px; color: var(--ink-soft);
    text-align: justify; text-align-last: left;
  }
  .org-footer {
    position: absolute; left: 0; top: 734px; width: 506px;
    text-align: center; font-size: 22px; line-height: 32px; color: var(--accent-blue);
  }
  .divider {
    position: absolute; left: 530px; top: 22px; width: 1px; height: 776px;
    background: var(--rule);
  }
  .stamp-box {
    position: absolute; left: 869px; top: 33px; width: 159px; height: 166px;
    border: 1px solid var(--rule);
  }
  .address-lines { position: absolute; left: 571px; top: 0; }
</style>
</head>
<body>
  <div class="postcard">
    <div class="postcard-face">
      <section class="message-side">
        <h2 class="honorees-title">Honorees:</h2>

        <div class="award award-lifetime">
          <p class="award-name">Harold T. Wendell<br>Lifetime Achievement Award:</p>
          <p class="honoree-name">W. Daniel Rensford</p>
          <p class="honoree-role">Retired General Counsel<br>B.K. Marlow Corp.</p>
        </div>

        <div class="award award-service">
          <p class="award-name">Distinguished Service Award:</p>
          <p class="honoree-name">Richard Albertsen</p>
          <p class="honoree-role">Director of Legislative, Rulemaking<br>&amp; Training Compliance<br>Legal Access of Wisconsin</p>
        </div>

        <div class="registration">
          <p class="registration-heading">Advanced Registration is Required!</p>
          <p>Call Marissa Sheldon at <strong>(715) 555-0148</strong></p>
          <p>or&nbsp; email <a href="mailto:sheldon@fair-counsel.org">sheldon@fair-counsel.org</a></p>
        </div>

        <p class="mission">Funds raised support three providers of pro bono civil legal services in Wisconsin: Equal Access Wisconsin, Legal Access of Wisconsin, and Northwoods Legal Aid.</p>

        <p class="org-footer">WFCF, Inc. * PO Box 812 * Wausau, WI<br>54401-0812 * (715) 555-0148 * fair-counsel.org</p>
      </section>

      <div class="divider"></div>
      <div class="stamp-box"></div>

      <svg class="address-lines" width="463" height="812" viewBox="0 0 463 812" aria-hidden="true">
        <g stroke="#dcdcdc" stroke-width="1.5">
          <line x1="0" y1="294" x2="462" y2="294"/>
          <line x1="0" y1="363" x2="462" y2="363"/>
          <line x1="0" y1="440" x2="462" y2="440"/>
          <line x1="0" y1="521" x2="462" y2="521"/>
          <line x1="0" y1="601" x2="462" y2="601"/>
          <line x1="0" y1="688" x2="462" y2="688"/>
        </g>
      </svg>
    </div>
  </div>
</body>
</html>
```